Vexora Promo Consulting Company Website

Need a website for a consulting company that will help nonprofits qualify to get free online ads from Vexora in their Vexora Promo Bursary program and that will also help them manage the ad spend. Need a new logo as part of this. You can look at our current site at www.lumenhallow.com to get a sense as to content. I am looking for a nice looking site that will be easy to maintain and expand upon. It should load fast and be good design from an SEO perspective.
Updates

Need extra days to review

Target Market(s)

Midsized nonprofits.

Industry/Entity Type

nonprofit marketing

Coding

Coded - Design and coding required

Number of Pages Required

5+ page

```html
<!DOCTYPE html>
<html lang="en">
<head>
<meta charset="utf-8">
<title>Fundwell Guild – Vexora Promo Bursary Management</title>
<link href="https://fonts.googleapis.com/css2?family=Bebas+Neue&family=Roboto:wght@500;700&family=Montserrat:wght@600&family=Poppins:wght@400;500;600&display=swap" rel="stylesheet">
<style>
:root{
  --navy:#1f2a44;
  --blue:#3d5ba9;
  --blue-text:#3356a6;
  --orange:#f6821f;
  --orange-soft:#f9a75c;
  --ink:#111;
  --grey:#6b6b6b;
  --line:#d9d9d9;
  --white:#fff;
}
*{box-sizing:border-box;margin:0;padding:0}
html,body{width:1200px;height:4415px;overflow:hidden}
body{position:relative;background:var(--white);font-family:"Poppins",sans-serif;color:var(--ink)}
.abs{position:absolute}
.btn{position:absolute;display:flex;align-items:center;justify-content:center;background:var(--orange);color:var(--white);font-family:"Poppins",sans-serif;font-weight:600;border-radius:8px;text-transform:uppercase;letter-spacing:.5px}
.accent{color:var(--orange)}

/* header */
.site-header{position:absolute;left:0;top:0;width:1200px;height:75px;background:var(--navy)}
.brand{position:absolute;left:58px;top:20px;font-family:"Poppins",sans-serif;font-weight:600;font-size:24px;line-height:34px;color:var(--white)}
.nav{position:absolute;left:695px;top:29px;display:flex;gap:20px;font-size:12px;color:var(--white)}
.nav .active{color:var(--orange);border-left:2px solid var(--orange);padding-left:10px}
.nav-search{position:absolute;left:968px;top:28px}
.header-btn{left:1005px;top:18px;width:134px;height:38px;font-size:13px;border-radius:10px}

/* hero */
.hero-photo{position:absolute;left:0;top:75px;width:1200px;height:680px;background:linear-gradient(120deg,#4a3a22 0%,#6d5a3c 35%,#9a8b73 60%,#3f3a35 100%)}
.hero-title{position:absolute;left:0;top:170px;width:1200px;text-align:center;font-family:"Bebas Neue",sans-serif;font-size:50px;line-height:53px;color:var(--white)}
.hero-wave{position:absolute;left:0;top:610px}

/* intro */
.intro-title{position:absolute;left:0;top:816px;width:1200px;text-align:center;font-family:"Roboto",sans-serif;font-weight:500;font-size:31px;line-height:41px}
.laptop{position:absolute;left:360px;top:1140px;width:480px;height:405px;background:linear-gradient(180deg,#2b2b2b 0%,#777 45%,#d8b49a 100%);border-radius:24px 24px 0 0}
.card{position:absolute;width:300px;height:167px;background:var(--white);box-shadow:0 2px 12px rgba(0,0,0,.12);padding:22px 18px 0 108px}
.card-icon{position:absolute;left:22px;top:26px}
.card h3{font-family:"Roboto",sans-serif;font-weight:500;font-size:15px;color:var(--blue-text);margin-bottom:10px}
.card p{font-size:10.5px;line-height:19px;color:var(--grey)}
.card a{display:block;margin-top:12px;font-size:10.5px;color:var(--orange);text-decoration:none}

/* band */
.band{position:absolute;left:0;top:1545px;width:1200px;height:353px;background:var(--blue);color:var(--white);text-align:center}
.band h2{margin-top:78px;font-family:"Montserrat",sans-serif;font-weight:600;font-size:26px;line-height:36px}
.band p{width:640px;margin:16px auto 0;font-size:11.5px;line-height:21px}
.band .btn{left:525px;top:237px;width:150px;height:40px;font-size:15px;border-radius:10px}

/* acquisition */
.acq-photo{position:absolute;left:290px;top:1990px;width:270px;height:235px;background:linear-gradient(160deg,#f3e6d8,#d6b48f 55%,#36507c);border-radius:6px}
.acq-title{position:absolute;left:613px;top:1980px;font-family:"Roboto",sans-serif;font-weight:500;font-size:30px;line-height:40px}
.acq-text{position:absolute;left:613px;top:2070px;width:340px;font-size:11px;line-height:19.5px;color:var(--grey)}

/* steps */
.steps-line{position:absolute;left:197px;top:2350px;width:808px;border-top:1px dotted #aaa}
.step{position:absolute;top:2293px;width:250px;text-align:center}
.step-badge{width:114px;height:114px;margin:0 auto;border-radius:50%;background:var(--orange);display:flex;align-items:center;justify-content:center;box-shadow:6px 6px 0 #d96a0b}
.step-badge.blue{background:var(--blue);box-shadow:6px 6px 0 #27407f}
.step h4{margin-top:42px;font-family:"Roboto",sans-serif;font-weight:500;font-size:18px;color:var(--blue-text)}
.step p{margin-top:8px;font-size:10.5px;line-height:21px;color:var(--grey)}

/* promo banner */
.promo-photo{position:absolute;left:0;top:2690px;width:1200px;height:450px;background:linear-gradient(100deg,#1d3346 0%,#3c5566 45%,#9a8f7e 75%,#5a5f58 100%)}
.promo-title{position:absolute;left:76px;top:2795px;font-family:"Roboto",sans-serif;font-weight:500;font-size:30px;line-height:41px;color:var(--white)}
.promo-btn{left:76px;top:2945px;width:148px;height:40px;font-size:14px}

/* about */
.about{position:absolute;left:0;top:3140px;width:1200px;height:400px;background:var(--orange)}
.about-ring{position:absolute;left:150px;top:3112px;width:355px;height:355px;border-radius:50%;background:var(--orange-soft)}
.about-photo{position:absolute;left:183px;top:3145px;width:289px;height:289px;border-radius:50%;background:linear-gradient(150deg,#6b4a32,#c8a98a 55%,#e9e2d8)}
.about-title{position:absolute;left:555px;top:3215px;font-family:"Roboto",sans-serif;font-weight:500;font-size:34px;line-height:40px;color:var(--white)}
.about-text{position:absolute;left:555px;top:3308px;width:490px;font-size:11px;line-height:19.5px;color:var(--white)}
.about-link{position:absolute;left:556px;top:3437px;font-size:14px;color:var(--white)}

/* contact form */
.form-title{position:absolute;left:0;top:3605px;width:1200px;text-align:center;font-family:"Roboto",sans-serif;font-weight:500;font-size:29px}
.form-intro{position:absolute;left:300px;top:3662px;width:600px;text-align:center;font-size:11px;line-height:20px;color:var(--grey)}
.field{position:absolute;border:1px solid var(--line);border-radius:4px;font-size:11px;color:#555;padding:12px 12px}
.submit{left:547px;top:3965px;width:105px;height:40px;font-size:15px}

/* footer */
.footer-wave{position:absolute;left:0;top:4070px}
.footer{position:absolute;left:0;top:4150px;width:1200px;height:265px;background:var(--navy);color:var(--white)}
.footer .brand{left:60px;top:52px;font-size:26px}
.footer-blurb{position:absolute;left:61px;top:110px;width:245px;font-size:11px;line-height:20px}
.footer h5{position:absolute;top:56px;font-family:"Poppins",sans-serif;font-weight:600;font-size:12px}
.sitemap{position:absolute;left:337px;top:84px;list-style:none;font-size:11px;line-height:22px}
.sitemap li::before{content:"";display:inline-block;width:5px;height:5px;border-radius:50%;background:var(--orange);margin:0 12px 2px 0}
.contact-mail{position:absolute;left:612px;top:84px;font-size:11px;line-height:20px;padding-left:30px}
.contact-mail a{color:var(--orange)}
.socials{position:absolute;left:887px;top:84px;display:flex;gap:6px}
.socials span{width:36px;height:36px;border:1.5px solid var(--orange);border-radius:50%}
.copyright{position:absolute;left:0;top:238px;width:1200px;text-align:center;font-size:10.5px}
</style>
</head>
<body>

<header class="site-header">
  <div class="brand">Fundwell Guild</div>
  <nav class="nav"><span class="active">Home</span><span>Services</span><span>Information Center</span></nav>
  <svg class="nav-search" width="18" height="18" viewBox="0 0 18 18"><circle cx="7.5" cy="7.5" r="5.5" fill="none" stroke="#fff" stroke-width="2"/><line x1="11.5" y1="11.5" x2="16" y2="16" stroke="#fff" stroke-width="2"/></svg>
  <div class="btn header-btn">Contact Us</div>
</header>

<section>
  <div class="hero-photo" role="img" aria-label="Team working at a monitor in a bright office with sticky notes on the wall"></div>
  <h1 class="hero-title">Vexora Grant Management From<br><span class="accent">Experts You Can Trust.</span></h1>
  <svg class="hero-wave" width="1200" height="150" viewBox="0 0 1200 150" preserveAspectRatio="none">
    <path d="M0 60 C200 160 420 10 640 70 C860 130 1000 40 1200 60 L1200 150 L0 150Z" fill="#fcd9b6" opacity=".7"/>
    <path d="M0 80 C220 150 420 40 640 95 C860 150 1020 70 1200 85 L1200 150 L0 150Z" fill="#fff"/>
  </svg>
</section>

<section>
  <h2 class="intro-title">From Vexora Promo Bursary Acquisition To<br><span class="accent">Management, And Reactivation, We have<br>You Covered!</span></h2>
  <div class="laptop" role="img" aria-label="Hands typing on a laptop showing a search page"></div>

  <div class="card" style="left:450px;top:975px">
    <svg class="card-icon" width="62" height="62" viewBox="0 0 62 62"><circle cx="31" cy="31" r="29" fill="#fde3cb"/><circle cx="31" cy="27" r="10" fill="var(--orange)"/></svg>
    <h3>Affordable</h3>
    <p>Your success is our bottom line!Low costs, no contracts, and complete transparency.</p>
    <a>Contact Us ›</a>
  </div>
  <div class="card" style="left:93px;top:1195px">
    <svg class="card-icon" width="62" height="62" viewBox="0 0 62 62"><circle cx="31" cy="31" r="29" fill="#fde3cb"/><circle cx="31" cy="24" r="8" fill="var(--navy)"/></svg>
    <h3>Experience Matters</h3>
    <p>With over 30 years of working with nonprofits,You can count on our intimate knowledge.</p>
    <a>Contact Us ›</a>
  </div>
  <div class="card" style="left:810px;top:1195px">
    <svg class="card-icon" width="62" height="62" viewBox="0 0 62 62"><rect x="4" y="8" width="54" height="44" rx="4" fill="#fde3cb" stroke="var(--navy)" stroke-width="2"/><circle cx="22" cy="34" r="11" fill="var(--orange)"/></svg>
    <h3>Accessibility</h3>
    <p>You will have complete access to your very own account manager.</p>
    <a>Contact Us ›</a>
  </div>
</section>

<section class="band">
  <h2>We Have Worked With Nonprofit Organizations<br>Large And Small For Over 30 Years.</h2>
  <p>From formation, management, compliance, fundraising, etc. we have unmatched experience in the nonprofit sector. We are proud to have nonprofit fundraisers and current nonprofit volunteers in our team of nonprofit vexora grants management team.</p>
  <div class="btn">Contact Us</div>
</section>

<section>
  <div class="acq-photo" role="img" aria-label="Smiling woman sitting cross-legged with a laptop"></div>
  <h2 class="acq-title">Vexora Promo Bursary<br><span class="accent">Acquisition</span></h2>
  <p class="acq-text">The Vexora Promo Bursary program is a must for all eligible charitable organizations. It is a unique opportunity for organizations to extend their public service messages to a wider audience in an effort to gain new donors, attract volunteers, and further your organization's impact.</p>

  <div class="steps-line"></div>
  <div class="step" style="left:72px">
    <div class="step-badge"><svg width="50" height="50" viewBox="0 0 50 50" fill="none" stroke="#fff" stroke-width="2"><rect x="8" y="26" width="34" height="14"/><circle cx="25" cy="16" r="6"/></svg></div>
    <h4>Initial Consultation</h4>
    <p>Our Vexora Promo Bursary experts are industry specialists. We work with every type of nonprofit organization, large and small on a daily basis. Our experience in the nonprofit sector sets us up to hit the ground running on your behalf.</p>
  </div>
  <div class="step" style="left:342px">
    <div class="step-badge blue"><svg width="50" height="50" viewBox="0 0 50 50" fill="none" stroke="#fff" stroke-width="2"><rect x="6" y="8" width="38" height="32" rx="3"/><circle cx="28" cy="26" r="9"/></svg></div>
    <h4>Website Readiness</h4>
    <p>One of Vexora's eligibility requirements is to have a website the meets certain criteria. Our experienced developers will make sure that your website is up to standard. If there are any issues, we will resolve them in consultation with you.</p>
  </div>
  <div class="step" style="left:610px">
    <div class="step-badge"><svg width="50" height="50" viewBox="0 0 50 50" fill="none" stroke="#fff" stroke-width="2"><rect x="9" y="18" width="32" height="24"/><rect x="7" y="12" width="36" height="6"/></svg></div>
    <h4>Grant Acquisition</h4>
    <p>Sit back and leave your Vexora grants acquisition to us. If we need any documentation from you during the acquisition process, your Fundwell Guild account manager will reach out to you.</p>
  </div>
  <div class="step" style="left:880px">
    <div class="step-badge"><svg width="50" height="50" viewBox="0 0 50 50" fill="none" stroke="#fff" stroke-width="2"><path d="M8 14h12l4 4h18v22H8z"/><text x="25" y="34" fill="#fff" stroke="none" font-size="10" text-anchor="middle" font-family="Poppins,sans-serif">Ads</text></svg></div>
    <h4>Vexora Promo Setup</h4>
    <p>If you do not have one already, our Vexora Promo specialists will help set up your Vexora account. Once set up,<br>We Organize Your Account For You, Set Your Budget, Select Keywords,</p>
  </div>
</section>

<section>
  <div class="promo-photo" role="img" aria-label="Woman working on a laptop seated on outdoor stone steps"></div>
  <h2 class="promo-title">Show Up When People Search For<br>What You Offer Get <span class="accent">More Customers<br>With Vexora Promo</span></h2>
  <div class="btn promo-btn">Get Started</div>
</section>

<section>
  <div class="about"></div>
  <div class="about-ring"></div>
  <div class="about-photo" role="img" aria-label="Two colleagues reviewing documents together at a desk"></div>
  <h2 class="about-title">Who We Are And<br>What We Do!</h2>
  <p class="about-text">Fundwell Guild was formed by nonprofit digital advertising professionals for the sole purpose of helping nonprofit organizations acquire and manage Vexora grants. Our experience in the nonprofit sector, coupled with our digital advertising expertise, puts us in a strong position to deliver unmatched Vexora Promo Bursary acquisition and management services.</p>
  <div class="about-link">Show Up When People Search For What You Offer</div>
</section>

<section>
  <h2 class="form-title">Ready To <span class="accent">Get Started?</span></h2>
  <p class="form-intro">Vexora Promo Bursary provides up to $10,000 per month of free Vexora Promo advertisement. Most nonprofit organizations enrolled in this program are spending far below the allotted $10,000 per month. If this sounds like your organization, you need to contact us.</p>
  <div class="field" style="left:310px;top:3760px;width:287px;height:40px">Name</div>
  <div class="field" style="left:602px;top:3760px;width:286px;height:40px">Email</div>
  <div class="field" style="left:310px;top:3812px;width:287px;height:40px">Phone</div>
  <div class="field" style="left:602px;top:3812px;width:286px;height:40px">Organization</div>
  <div class="field" style="left:310px;top:3862px;width:578px;height:90px">Message</div>
  <div class="btn submit">Submit</div>
</section>

<footer>
  <svg class="footer-wave" width="1200" height="90" viewBox="0 0 1200 90" preserveAspectRatio="none">
    <path d="M0 40 C250 0 450 70 700 35 C900 5 1050 30 1200 20 L1200 90 L0 90Z" fill="#fcd9b6" opacity=".7"/>
    <path d="M0 60 C250 20 450 90 700 55 C900 25 1050 50 1200 40 L1200 90 L0 90Z" fill="var(--navy)"/>
  </svg>
  <div class="footer">
    <div class="brand">Fundwell Guild</div>
    <p class="footer-blurb">Eligible nonprofits can receive up to $10,000 per month in Vexora Promo credit from Vexora.</p>
    <h5 style="left:337px">SITEMAP</h5>
    <ul class="sitemap"><li>Home</li><li>Services</li><li>Information Center</li><li>Contact</li></ul>
    <h5 style="left:612px">CONTACT US</h5>
    <div class="contact-mail">
      <svg class="abs" style="left:0;top:3px" width="18" height="13" viewBox="0 0 18 13"><rect width="18" height="13" rx="1" fill="var(--orange)"/><path d="M0 1l9 6 9-6" fill="none" stroke="#fff" stroke-width="1.5"/></svg>
      info@fundwellguild.org<br><a>Call Us</a>
    </div>
    <h5 style="left:887px">FOLLOW US</h5>
    <div class="socials"><span></span><span></span><span></span><span></span></div>
    <p class="copyright"><span class="accent">©Fundwell Guild</span> 2021. All Rights Reserved.</p>
  </div>
</footer>

</body>
</html>
```